Dental Co needs single page print ad

Dental company needs a 1 page ad for trade magazines.
I am uploading an example of what we want (words). We need you to make it look great. It can include people or not.
The uploaded ad isn't there to be copied, just to kind of frame what we are thinking. We are open to any design
One page ad
Size 1)

Trim Size - 8 x 10.5
Bleed Size - 8.25 x 10.75
Live Area - 7 x 10

Size 2)

Trim - 8 x 10.875
Bleed - 8.25 x 11.125
Live Area - 7 x 9.875

BRIX Brand Hex #'s

Orange - ff6319
Teal - 56b1bf
Lt. Teal - aed9da
Blue: #38394B

Target Market(s)

Dentists

Requirements
Must have
• BRIX Logo, pic of the sensor (called VANT)
Use the brand hex colors:
Orange - ff6319
Teal - 56b1bf
Lt. Teal - aed9da
Blue: #38394B

```html
<!DOCTYPE html>
<html lang="en">
<head>
<meta charset="utf-8">
<title>BRIX Imaging – VANT Sensor Subscription Ad</title>
<link rel="stylesheet" href="https://fonts.googleapis.com/css2?family=Bebas+Neue&family=Montserrat:wght@400;600;700;800&family=Dancing+Script:wght@500&display=swap">
<style>
  :root {
    --orange: #f26522;
    --orange-light: #ff8a3d;
    --navy: #2a2560;
    --purple: #4a2a5e;
    --white: #ffffff;
    --photo-light: #e6e6e6;
    --photo-mid: #b9b9b9;
    --sensor: #4a4b7a;
  }
  * { margin: 0; padding: 0; box-sizing: border-box; }
  html, body { width: 869px; height: 1200px; overflow: hidden; background: var(--white); }
  .ad { position: relative; width: 869px; height: 1200px; overflow: hidden; background: var(--white); font-family: "Montserrat", sans-serif; }
  .ad__shapes { position: absolute; inset: 0; }

  .brand { position: absolute; left: 560px; top: 44px; display: flex; align-items: center; gap: 12px; }
  .brand__mark { width: 22px; height: 22px; background: var(--orange); }
  .brand__name { font-family: "Montserrat", sans-serif; font-weight: 800; font-size: 74px; line-height: 1; color: var(--navy); letter-spacing: -1px; }

  .headline { position: absolute; left: 24px; top: 748px; font-family: "Bebas Neue", sans-serif; font-size: 47px; line-height: 46px; color: var(--orange); }
  .headline__aside { font-family: "Dancing Script", cursive; font-size: 21px; color: var(--navy); margin-left: 6px; }

  .price { position: absolute; left: 24px; display: flex; align-items: baseline; gap: 14px; }
  .price--fee { top: 912px; }
  .price--monthly { top: 982px; }
  .price__amount { font-family: "Bebas Neue", sans-serif; font-size: 44px; line-height: 1; color: var(--orange); }
  .price__label { font-size: 23px; color: var(--navy); font-weight: 400; letter-spacing: 0.2px; }
  .price__rule { position: absolute; left: 24px; top: 962px; width: 126px; height: 4px; background: var(--orange); }

  .benefits { position: absolute; left: 605px; top: 622px; list-style: none; }
  .benefits__item { display: flex; align-items: center; height: 52px; margin-bottom: 17.5px; }
  .benefits__num { width: 52px; height: 52px; border: 2px solid var(--white); border-radius: 50%; display: flex; align-items: center; justify-content: center; color: var(--white); font-weight: 700; font-size: 22px; flex: none; }
  .benefits__text { margin-left: 26px; color: var(--white); font-size: 15px; line-height: 19px; }

  .cta { position: absolute; left: 34px; top: 1058px; color: var(--white); }
  .cta__label { font-family: "Bebas Neue", sans-serif; font-size: 50px; line-height: 1; color: #ffb07a; }
  .cta__phone { font-weight: 700; font-size: 35px; line-height: 1.2; border-bottom: 2px solid var(--white); padding-bottom: 1px; display: inline-block; }
  .cta__web { font-size: 21px; line-height: 1.3; }

  .product-name { position: absolute; left: 560px; top: 1082px; font-weight: 800; font-size: 96px; line-height: 1; color: var(--navy); letter-spacing: 1px; }
</style>
</head>
<body>
<main class="ad">
  <svg class="ad__shapes" width="869" height="1200" viewBox="0 0 869 1200">
    <defs>
      <linearGradient id="photoTone" x1="0" y1="0" x2="1" y2="1">
        <stop offset="0" stop-color="#f0f0f0"/>
        <stop offset="0.5" stop-color="#cfcfcf"/>
        <stop offset="1" stop-color="#e4e4e4"/>
      </linearGradient>
      <linearGradient id="portraitTone" x1="0" y1="0" x2="0" y2="1">
        <stop offset="0" stop-color="#f26522"/>
        <stop offset="0.55" stop-color="#c9a08a"/>
        <stop offset="1" stop-color="#9a9a9a"/>
      </linearGradient>
      <linearGradient id="ctaTone" x1="0" y1="0" x2="1" y2="0">
        <stop offset="0" stop-color="#f26522"/>
        <stop offset="0.55" stop-color="#5a2c5c"/>
        <stop offset="1" stop-color="#2a2560"/>
      </linearGradient>
    </defs>

    <g role="img" aria-label="Black and white photo of fingers holding the navy VANT intra-oral sensor">
      <polygon points="0,0 869,0 869,433 0,528" fill="url(#photoTone)"/>
      <ellipse cx="440" cy="360" rx="145" ry="110" fill="var(--sensor)" opacity="0.35"/>
    </g>

    <polygon points="417,576 869,443 869,455 417,588" fill="var(--purple)"/>
    <polygon points="0,508 62,532 62,542 0,520" fill="var(--orange)"/>

    <circle cx="238" cy="569" r="157" fill="var(--white)"/>
    <circle cx="238" cy="569" r="147" fill="url(#portraitTone)" role="img" aria-label="Portrait photo of a smiling woman pointing at her smile"/>

    <polygon points="496,661 534,661 475,788 534,915 496,915 423,788" fill="var(--orange)"/>
    <polygon points="596,576 869,576 869,1001 596,1001 478,788" fill="var(--navy)"/>

    <polygon points="342,1050 360,1050 458,1200 436,1200" fill="var(--orange)"/>
    <polygon points="0,1050 340,1050 432,1200 0,1200" fill="url(#ctaTone)"/>
  </svg>

  <div class="brand">
    <span class="brand__name">BRIX</span>
    <span class="brand__mark"></span>
  </div>

  <h1 class="headline">A subscription option<br>for intra-oral sensors<br>is dumb.<span class="headline__aside">(Until You do The Math)</span></h1>

  <p class="price price--fee"><span class="price__amount">$1,999</span><span class="price__label">ONE-TIME SIGN UP FEE</span></p>
  <span class="price__rule"></span>
  <p class="price price--monthly"><span class="price__amount">$139/MO</span><span class="price__label">CANCEL ANYTIME</span></p>

  <ol class="benefits">
    <li class="benefits__item"><span class="benefits__num">1</span><span class="benefits__text">Lifetime $0<br>deductible warranty</span></li>
    <li class="benefits__item"><span class="benefits__num">2</span><span class="benefits__text">Unlimited support<br>&amp; upgrades</span></li>
    <li class="benefits__item"><span class="benefits__num">3</span><span class="benefits__text">Direct integration<br>w/all major software</span></li>
    <li class="benefits__item"><span class="benefits__num">4</span><span class="benefits__text">Affordable enough<br>for every op</span></li>
    <li class="benefits__item"><span class="benefits__num">5</span><span class="benefits__text">Preserve your<br>capital</span></li>
  </ol>

  <div class="cta">
    <p class="cta__label">Call now</p>
    <p class="cta__phone">+1 555-010-4821</p>
    <p class="cta__web">www.briximaging.com</p>
  </div>

  <p class="product-name">VANT</p>
</main>
</body>
</html>
```